New business card for my lawn and landscape business

Dorrin Yard and Building is a full-service lawn care, landscaping, and light construction company serving Paragould and the Northeast Arkansas region. The business is owned and operated by Marcus Toller, with a reputation for hands-on, detail-oriented service, dependable crews, and quality results for both residential and commercial clients. A well regarded business with great reviews.
Owner Marcus Toller
Dorrinyardandbuilding.example

Target Market(s)

Commercial, Middle, and upper class in north east Arkansas

Industry/Entity Type

Lawn maintenance and landscape

Contact Information for Business Card

Dorrin Yard And Building Professional lawn care, landscaping, and property improvement in Northeast Arkansas. • lawn maintenance •lawn treatments and weed control • exterior projects • Custom landscape design & installation • Sod, trees, rock & drainage solutions • Residential & commercial services Reliable. Detailed. Done right.

Requirements
Must have
• Business name, service area, list of some of our services, clean design that represents
Nice to have
• Unique. Different design element than just grass because its already in n the logo. Picture of a warm season (south) lawn or landscape. Pictures of the type of work we do

```html
<!DOCTYPE html>
<html lang="en">
<head>
<meta charset="utf-8">
<title>Dorrin Yard and Building – Business Card</title>
<link href="https://fonts.googleapis.com/css2?family=Poppins:wght@300;400;500;600;700&display=swap" rel="stylesheet">
<style>
  :root {
    --page: #e7e8ea;
    --card-black: #050709;
    --green: #76b843;
    --white: #ffffff;
    --silver: #b9babd;
    --text-soft: #e9ecee;
  }
  * { box-sizing: border-box; margin: 0; padding: 0; }
  html, body {
    width: 1195px; height: 1200px; overflow: hidden;
    background: var(--page);
    font-family: "Poppins", sans-serif;
  }
  .card {
    position: absolute; left: 307px; width: 580px; height: 332px; overflow: hidden;
  }
  .card-front { top: 188px; background: var(--card-black); }
  .card-back { top: 629px; }

  .trim-band { position: absolute; left: 0; bottom: 0; width: 580px; height: 19px; display: block; }

  /* Front */
  .brand-mark {
    position: absolute; left: 34px; top: 134px; width: 236px;
    display: flex; align-items: center; gap: 12px;
  }
  .brand-ring {
    flex: none; width: 44px; height: 44px; border-radius: 50%;
    border: 3px solid var(--silver);
  }
  .brand-name {
    color: var(--green); font-weight: 600; font-size: 21px; line-height: 1.15;
  }
  .owner-name {
    position: absolute; right: 34px; top: 24px;
    color: var(--green); font-weight: 700; font-size: 24px; letter-spacing: 1px; line-height: 1.2;
  }
  .owner-title {
    position: absolute; right: 34px; top: 54px;
    color: var(--white); font-weight: 700; font-size: 14px; letter-spacing: 1px; line-height: 1.2;
  }
  .contact-list { position: absolute; right: 34px; top: 115px; list-style: none; }
  .contact-item {
    display: flex; justify-content: flex-end; align-items: center; gap: 10px;
    height: 21.5px; color: var(--white); font-weight: 400; font-size: 10px; letter-spacing: .5px;
  }
  .contact-icon { width: 15px; height: 15px; flex: none; }
  .contact-divider {
    position: absolute; left: 328px; top: 191px; width: 218px; height: 1px;
    background: linear-gradient(to right, #5c5e62, #d7d8da);
  }
  .locations-title {
    position: absolute; right: 35px; top: 200px;
    color: var(--green); font-weight: 600; font-size: 15px; letter-spacing: .6px; line-height: 1.2;
  }
  .location {
    position: absolute; color: var(--white); font-weight: 400; font-size: 9.5px; letter-spacing: .5px;
    display: flex; align-items: center; gap: 6px; line-height: 1.2;
  }
  .location::before {
    content: ""; width: 5px; height: 5px; border-radius: 50%; background: var(--green);
  }
  .service-area {
    position: absolute; right: 32px; top: 277px;
    color: var(--green); font-weight: 400; font-size: 11.5px; letter-spacing: 3px; line-height: 1.2;
  }

  /* Back */
  .lawn-photo {
    position: absolute; inset: 0;
    background:
      radial-gradient(ellipse 40% 20% at 62% 30%, rgba(150,140,120,.45), transparent 70%),
      linear-gradient(to bottom, #3a2e22 0%, #4e4a40 20%, #3a3a30 33%, #2f4a2a 42%, #2c4b29 65%, #1c351d 100%);
  }
  .back-brand {
    position: absolute; left: 0; right: 0; top: 90px;
    display: flex; justify-content: center; align-items: center; gap: 12px;
  }
  .back-brand .brand-ring { width: 40px; height: 40px; }
  .back-brand .brand-name { color: var(--text-soft); font-size: 22px; }
  .back-divider {
    position: absolute; left: 34px; top: 183px; width: 513px; height: 2px;
    background: linear-gradient(to right, #f0f0f0, #a9aaad 70%, #6b6c70);
  }
  .services-copy {
    position: absolute; left: 22px; right: 22px; top: 196px;
    text-align: center; color: var(--text-soft);
    font-weight: 300; font-size: 14px; line-height: 19.7px; letter-spacing: .5px;
  }
  .bullet { color: var(--green); font-size: 15px; line-height: 1; }
</style>
</head>
<body>

<section class="card card-front">
  <div class="brand-mark">
    <span class="brand-ring"></span>
    <span class="brand-name">Dorrin Yard and Building</span>
  </div>

  <h1 class="owner-name">Marcus Toller</h1>
  <p class="owner-title">Owner</p>

  <ul class="contact-list">
    <li class="contact-item">(555) 014-2268
      <svg class="contact-icon" viewBox="0 0 16 16"><circle cx="8" cy="8" r="7" fill="none" stroke="#76b843" stroke-width="1"/><path d="M5.3 4.6c.4-.3.8-.2 1 .2l.6 1.1c.2.4.1.7-.2.9l-.4.3c.4.9 1 1.5 1.9 1.9l.3-.4c.2-.3.6-.4.9-.2l1.1.6c.4.2.5.6.2 1l-.5.6c-.4.4-1 .5-1.6.2-1.7-.8-2.9-2-3.7-3.7-.3-.6-.2-1.2.2-1.6z" fill="#76b843"/></svg>
    </li>
    <li class="contact-item">Cedar Hollow, AR 70999
      <svg class="contact-icon" viewBox="0 0 16 16"><circle cx="8" cy="8" r="7" fill="none" stroke="#76b843" stroke-width="1"/><path d="M8 3.6a2.8 2.8 0 0 0-2.8 2.8c0 2.1 2.8 5.2 2.8 5.2s2.8-3.1 2.8-5.2A2.8 2.8 0 0 0 8 3.6z" fill="#76b843"/><circle cx="8" cy="6.4" r="1.1" fill="#050709"/></svg>
    </li>
    <li class="contact-item">www.dorrinyardandbuilding.example
      <svg class="contact-icon" viewBox="0 0 16 16" fill="none" stroke="#76b843" stroke-width=".8"><circle cx="8" cy="8" r="7"/><ellipse cx="8" cy="8" rx="3" ry="7"/><path d="M1 8h14M2 4.5h12M2 11.5h12"/></svg>
    </li>
  </ul>

  <div class="contact-divider"></div>
  <h2 class="locations-title">Locations Served</h2>
  <p class="location" style="left:330px;top:229px">Ashbury, AR</p>
  <p class="location" style="left:461px;top:229px">Millbrook, AR</p>
  <p class="location" style="left:330px;top:253px">Cedar Hollow, AR</p>
  <p class="location" style="left:446px;top:253px">Pine Crossing, AR</p>
  <p class="service-area">Serving Northeast Arkansas</p>

  <svg class="trim-band" viewBox="0 0 580 19" preserveAspectRatio="none">
    <defs>
      <linearGradient id="steelFront" x1="0" x2="1"><stop offset="0" stop-color="#c9cacc"/><stop offset="1" stop-color="#6e6f73"/></linearGradient>
      <linearGradient id="whiteFront" x1="0" x2="1"><stop offset="0" stop-color="#ffffff"/><stop offset="1" stop-color="#c4c5c7"/></linearGradient>
    </defs>
    <rect x="0" y="0" width="580" height="19" fill="url(#whiteFront)"/>
    <path d="M0 8H322L318 12H0z" fill="#050709"/>
    <path d="M332 0H580V19H312L321 12H319L327 5z" fill="url(#steelFront)"/>
    <path d="M332 0L320 11H316L328 0z" fill="#050709"/>
  </svg>
</section>

<section class="card card-back">
  <div class="lawn-photo" role="img" aria-label="Photo of a warm-season lawn at dusk with autumn trees behind"></div>

  <div class="back-brand">
    <span class="brand-ring"></span>
    <span class="brand-name">Dorrin Yard and Building</span>
  </div>

  <div class="back-divider"></div>

  <p class="services-copy">
    Dorrin Yard And Building Professional lawn care, landscaping, and property improvement in Northeast Arkansas <span class="bullet">●</span> Lawn maintenance, lawn treatments and weed control <span class="bullet">●</span> Exterior projects <span class="bullet">●</span> Custom landscape design &amp; installation <span class="bullet">●</span> Sod, trees, rock &amp; drainage solutions <span class="bullet">●</span> Residential &amp; commercial services Reliable. Detailed. Done right
  </p>

  <svg class="trim-band" viewBox="0 0 580 19" preserveAspectRatio="none">
    <defs>
      <linearGradient id="steelBack" x1="0" x2="1"><stop offset="0" stop-color="#c9cacc"/><stop offset="1" stop-color="#6e6f73"/></linearGradient>
      <linearGradient id="whiteBack" x1="0" x2="1"><stop offset="0" stop-color="#ffffff"/><stop offset="1" stop-color="#c4c5c7"/></linearGradient>
    </defs>
    <rect x="0" y="0" width="580" height="19" fill="url(#whiteBack)"/>
    <path d="M0 8H322L318 12H0z" fill="#1a2e1c"/>
    <path d="M332 0H580V19H312L321 12H319L327 5z" fill="url(#steelBack)"/>
    <path d="M332 0L320 11H316L328 0z" fill="#1a2e1c"/>
  </svg>
</section>

</body>
</html>
```